Property management company looking for modern card design

We at Blue Maple Holdings provides property management services for its residential and commercial properties, with expertise in all categories of multifamily, industrial and office projects throughout California.

We need a business card design that is professional and modern designed business card. In our field, clients get hundreds of business cards, we would like our card to stand out.

Please avoid small print.

Target Market(s)

Professionals and high end clients

Industry/Entity Type

Financial Planning

Contact Information for Business Card

Company Name: Blue Maple Holdings, Name, email, license #, phone number, website bluemapleholdings.example

Font styles to use
Sans Serif

Requirements
Must have
• The card design needs to be adaptable because there is a possibly we will be expanding into different sectors other than real estate. The card design should be focused on financial planning and asset management.
Nice to have
• Modern and simple business card. Eye catching. Non-standard size/shaped cards would be great.
• bluemapleholdings.example
Should not have
• Too many bright color or any pictures or shapes of real estate stuff.

```html
<!DOCTYPE html>
<html lang="en">
<head>
<meta charset="utf-8">
<title>Blue Maple Holdings – Business Card</title>
<link rel="stylesheet" href="https://fonts.googleapis.com/css2?family=Open+Sans:wght@400;600;700&display=swap">
<style>
  :root {
    --backdrop: #2b2b2d;
    --card: #fbfbfb;
    --ink-dark: #2a2a2a;
    --ink-mid: #555555;
    --ink-soft: #8a8a8a;
    --band: #e4e4e4;
  }
  * { box-sizing: border-box; margin: 0; padding: 0; }
  html, body {
    width: 1200px;
    height: 1000px;
    overflow: hidden;
    background: var(--backdrop);
    font-family: "Open Sans", Arial, sans-serif;
  }
  .card-set {
    position: absolute;
    inset: 0;
    display: flex;
    justify-content: center;
    align-items: center;
    gap: 60px;
  }
  .card {
    width: 400px;
    height: 700px;
    background: var(--card);
    position: relative;
    box-shadow: 0 12px 30px rgba(0,0,0,.45);
  }
  /* Contact side */
  .card-contact { padding: 150px 0 0 44px; }
  .person-name {
    font-size: 30px;
    font-weight: 700;
    letter-spacing: 2px;
    color: var(--ink-dark);
    text-transform: uppercase;
  }
  .person-title {
    display: inline-block;
    margin-top: 2px;
    font-size: 21px;
    color: var(--ink-mid);
    letter-spacing: .5px;
    padding-bottom: 6px;
    border-bottom: 2px solid var(--ink-dark);
  }
  .pattern-band {
    position: absolute;
    left: 0;
    right: 0;
    top: 300px;
    height: 10px;
    background: var(--band);
  }
  .contact-list {
    position: absolute;
    left: 44px;
    top: 400px;
    display: flex;
    flex-direction: column;
    gap: 22px;
  }
  .contact-label {
    font-size: 16px;
    color: var(--ink-mid);
    letter-spacing: 1px;
  }
  .contact-value {
    font-size: 17px;
    color: var(--ink-soft);
    line-height: 1.3;
  }
  /* Brand side */
  .card-brand {
    display: flex;
    flex-direction: column;
    align-items: center;
    justify-content: center;
    padding-bottom: 60px;
  }
  .brand-name {
    font-size: 30px;
    font-weight: 700;
    letter-spacing: 2px;
    color: var(--ink-dark);
    text-transform: uppercase;
    text-align: center;
    line-height: 1.25;
  }
  .brand-web {
    margin-top: 18px;
    font-size: 18px;
    font-weight: 600;
    color: var(--ink-mid);
  }
</style>
</head>
<body>
  <main class="card-set">
    <section class="card card-contact">
      <h1 class="person-name">Daniel Reyes</h1>
      <p class="person-title">Marketing Head</p>
      <div class="pattern-band" role="img" aria-label="Thin decorative chain-link band across the card"></div>
      <dl class="contact-list">
        <div><dt class="contact-label">MOBILE</dt><dd class="contact-value">+000 12345 6789</dd></div>
        <div><dt class="contact-label">EMAIL</dt><dd class="contact-value">daniel@bluemapleholdings.example</dd></div>
        <div><dt class="contact-label">WEB</dt><dd class="contact-value">bluemapleholdings.example</dd></div>
        <div><dt class="contact-label">Address</dt><dd class="contact-value">Your Street Address<br>New York, 1234</dd></div>
      </dl>
    </section>
    <section class="card card-brand">
      <p class="brand-name">Blue Maple<br>Holdings</p>
      <p class="brand-web">www.bluemapleholdings.example</p>
    </section>
  </main>
</body>
</html>
```